TRUCK WRAP DESIGN T&K SUPPLY

Create clean, elegant and attractive design with provided information.
It should include:
--Nice, clean and elegant background( either image hi quality or combination of colors).
--T&K Logo(attached), 555-314-2690, FALWICK COATINGS logo(attached), Established 1926.
-- Building Maintenance Supplies
-- Hardware, paints, plumbing, electrical supplies and janitorial supplies.

All this has to be on Passenger, Driver and Back sides. Logo and phone number on the front of the truck.

Colors

Designer to choose colors to be used in the design.

Requirements
Must have
• Create clean, elegant and attractive design with provided information.
• It should include:
• --Nice, clean and elegant background( either image hi quality or combination of colors).
• --T&K Logo(attached), 555-314-2690, FALWICK COATINGS logo(attached), Established 1926.
• -- Building Maintenance Supplies
• -- Hardware, paints, plumbing, electrical supplies and janitorial supplies.
• All this has to be on Passenger, Driver and Back sides. Logo and phone number on the front of the truck.

```html
<!DOCTYPE html>
<html lang="en">
<head>
<meta charset="utf-8">
<title>T&amp;K Supply – Truck Wrap Side Panel</title>
<link rel="stylesheet" href="https://fonts.googleapis.com/css2?family=Montserrat:wght@600;700;800&family=Oswald:wght@600&display=swap">
<style>
  :root {
    --stage: #ffffff;
    --wrap-yellow: #efab1d;
    --wrap-yellow-light: #f6bf2c;
    --panel-white: #f4f4f4;
    --brand-blue: #1b4a82;
    --brand-blue-dark: #143a68;
    --ink: #121212;
    --bullet-red: #c4112f;
    --phone-yellow: #f7b51b;
    --phone-edge: #1a1a1a;
    --pill-black: #111111;
    --on-dark: #ffffff;
  }
  * { box-sizing: border-box; margin: 0; padding: 0; }
  html, body {
    width: 1200px; height: 548px; overflow: hidden;
    background: var(--stage);
  }
  .canvas { position: relative; width: 1200px; height: 548px; }

  .side-panel {
    position: absolute; left: 24px; top: 52px;
    width: 960px; height: 370px;
    transform: scale(1.2); transform-origin: 0 0;
    font-family: "Montserrat", Arial, sans-serif;
  }
  .panel-shapes { position: absolute; inset: 0; }

  .worker-photo {
    position: absolute; left: 0; top: 0; width: 225px; height: 370px;
    background: linear-gradient(160deg, #2c4f86 0%, #6d87b3 30%, #d9a54a 55%, #e9c23b 70%, #222 88%, #8fa3bd 100%);
  }

  .headline {
    position: absolute; right: 355px; top: 50px;
    text-align: right; color: var(--brand-blue);
    font-weight: 800; font-size: 46px; line-height: 52px; letter-spacing: -0.5px;
  }

  .product-list {
    position: absolute; left: 628px; top: 60px; list-style: none;
    font-weight: 700; font-size: 17.5px; line-height: 24px; color: var(--ink);
  }
  .product-list li { position: relative; padding-left: 16px; }
  .product-list li::before {
    content: ""; position: absolute; left: 2px; top: 9px;
    width: 7px; height: 7px; border-radius: 50%; background: var(--bullet-red);
  }

  .partner-mark {
    position: absolute; left: 818px; top: 52px;
    display: flex; align-items: center; gap: 5px;
    font-weight: 700; font-size: 11px; color: var(--brand-blue-dark);
  }
  .partner-mark .square { width: 10px; height: 10px; background: var(--bullet-red); }

  .company-mark {
    position: absolute; left: 262px; top: 250px; width: 210px;
    display: flex; flex-direction: column; align-items: center; gap: 6px;
    font-weight: 800; font-size: 20px; color: var(--brand-blue);
  }
  .company-mark .circle { width: 46px; height: 46px; border-radius: 50%; background: var(--brand-blue); }

  .call-pill {
    position: absolute; left: 745px; top: 225px; width: 184px; height: 29px;
    border-radius: 7px; background: var(--pill-black); color: var(--on-dark);
    font-weight: 800; font-size: 19px; line-height: 29px; text-align: center;
  }

  .phone {
    position: absolute; right: 22px; top: 255px;
    font-family: "Oswald", "Arial Narrow", sans-serif; font-weight: 600;
    font-size: 74px; line-height: 90px; color: var(--phone-yellow);
    letter-spacing: 0.5px;
    -webkit-text-stroke: 2px var(--phone-edge); paint-order: stroke fill;
  }
</style>
</head>
<body>
<main class="canvas">
  <section class="side-panel" aria-label="T&amp;K Supply truck side wrap">
    <svg class="panel-shapes" viewBox="0 0 960 370" width="960" height="370" aria-hidden="true">
      <defs>
        <linearGradient id="yellowBand" x1="0" y1="0" x2="0" y2="1">
          <stop offset="0" stop-color="var(--wrap-yellow-light)"/>
          <stop offset="1" stop-color="var(--wrap-yellow)"/>
        </linearGradient>
      </defs>
      <rect class="band-yellow" width="960" height="370" fill="url(#yellowBand)"/>
      <path class="panel-white" fill="var(--panel-white)"
        d="M225,12 H350 Q360,12 366,20 L372,28 H770 Q780,28 782,38 L790,95 Q792,105 802,105 H950 Q958,105 958,113 V345 H225 Z"/>
      <path class="band-blue" fill="var(--brand-blue)"
        d="M565,200 H960 V370 H225 V349 H518 L553,210 Q556,200 565,200 Z"/>
    </svg>

    <div class="worker-photo" role="img" aria-label="Photo of a tradesman in a plaid shirt and tool belt holding a yellow hard hat and a toolbox"></div>

    <h1 class="headline">Building<br>Maintenance<br>Supplies</h1>

    <ul class="product-list">
      <li>Hardware.</li>
      <li>Paints.</li>
      <li>Plumbing.</li>
      <li>Electrical Supplies.</li>
      <li>Janitorial Supplies.</li>
    </ul>

    <div class="partner-mark"><span class="square"></span>FALWICK COATINGS</div>

    <div class="company-mark"><span class="circle"></span>T&amp;K SUPPLY</div>

    <div class="call-pill">CALL TODAY!</div>
    <div class="phone">555-314-2690</div>
  </section>
</main>
</body>
</html>
```